A start-up named "Corvath Therapeutics" - needs a new PowerPoint design

We need a new PowerPoint Design for an early-stage start-up named "Corvath Therapeutics" seeking to disrupt the current approach towards drug discovery within aging disorders.

We would like to build on Corvath's legacy, the founder of the modern science of genetics, by employing a multidisciplinary approach, experimenting, and providing elderly patients the attention they deserve.

We have selected the suffix "therapeutics" intentionally as it stands for (a medicine) the treatment of disease; the science of healing. Alzheimer’s treatment is a huge, urgent, unmet need:
- Shift from a disease-management system to a preventive medicine system
- Focus on increasing the health span, not only the life span

Target Market(s)

Pharma/ Biotech Executives Medical Institutions Healthcare professionals (MDs, nurses, payors, pharmacists, etc.) Patients

Industry/Entity Type

Healthcare

Other font styles liked:
• Celias

Colors
0054AA
0677BA
7BADD7
CADEEF
E8F1F8
E54698
E96AAD
F1A4CE
F9D9EA
FCEFF6
A7469A
B969AE
D3A5CF
EDDBEB
F8F0F9
6B429C
8869AF
B7A5CE
E3DAEB
F3F0F8

Requirements
Must have
• - differentiate from other companies named after Corvath - differentiate from other Pharma/ Biotech companies
Nice to have
• simplicity/ minimalist logo vivid colors gradient 3D Life-Sciences inspired Simple geometry Balance
Should not have
• mascot/ emblem watermark logo animated ink style nature-inspired inventive typography artistic chaos

```html
<!DOCTYPE html>
<html lang="en">
<head>
<meta charset="utf-8">
<title>Corvath Therapeutics – Presentation System</title>
<link rel="stylesheet" href="https://fonts.googleapis.com/css2?family=Montserrat:wght@500;600;700;800;900&family=Quicksand:wght@500;600;700&display=swap">
<style>
  :root {
    --stage: #000000;
    --plum-light: #86195f;
    --plum: #6a1149;
    --plum-deep: #520b38;
    --berry: #9c2470;
    --rose: #e0245e;
    --amber: #f2a21e;
    --amber-deep: #f39a1f;
    --white: #ffffff;
    --mist: #d9d9d9;
    --grey: #9a9a9a;
    --blush: #c993c1;
    --brand-ink: #7a1655;
  }
  * { margin: 0; padding: 0; box-sizing: border-box; }
  html, body { width: 890px; height: 1200px; overflow: hidden; background: var(--stage); }
  .deck { position: relative; width: 890px; height: 1200px; }
  .slide {
    position: absolute; width: 333px; height: 187px; overflow: hidden;
    background: radial-gradient(ellipse at 55% 40%, var(--plum-light) 0%, var(--plum) 55%, var(--plum-deep) 100%);
  }
  .slide.is-light { background: var(--white); }
  .slide svg { display: block; width: 100%; height: 100%; }
  .col-a { left: 100px; } .col-b { left: 457px; }
  .row-1 { top: 96px; } .row-2 { top: 301px; } .row-3 { top: 506px; } .row-4 { top: 711px; } .row-5 { top: 916px; }

  text { font-family: "Quicksand", sans-serif; font-weight: 600; fill: var(--white); }
  .brand-name { font-family: "Quicksand", sans-serif; font-weight: 700; fill: var(--brand-ink); }
  .brand-hero { font-family: "Quicksand", sans-serif; font-weight: 700; fill: var(--white); }
  .brand-faint { font-family: "Quicksand", sans-serif; font-weight: 700; fill: var(--blush); }
  .heading { font-family: "Montserrat", sans-serif; font-weight: 800; fill: var(--amber); }
  .heading-white { font-family: "Montserrat", sans-serif; font-weight: 800; fill: var(--white); }
  .stat { font-family: "Montserrat", sans-serif; font-weight: 700; fill: var(--white); }
  .stat-amber { font-family: "Montserrat", sans-serif; font-weight: 700; fill: var(--amber); }
  .label { font-family: "Montserrat", sans-serif; font-weight: 700; fill: var(--white); font-size: 5px; }
  .body { font-size: 6px; font-weight: 500; }
  .micro { font-size: 4.2px; font-weight: 500; }
  .agenda-topic { font-family: "Montserrat", sans-serif; font-weight: 800; fill: var(--amber); font-size: 5px; }
  .agenda-num { font-family: "Montserrat", sans-serif; font-weight: 900; fill: var(--white); font-size: 30px; }
  .year { font-family: "Montserrat", sans-serif; font-weight: 700; fill: var(--white); font-size: 10px; }
</style>
</head>
<body>
<svg width="0" height="0" style="position:absolute" aria-hidden="true">
  <defs>
    <linearGradient id="ringGrad" x1="0" y1="0" x2="1" y2="0">
      <stop offset="0" stop-color="#f2a21e"/>
      <stop offset="1" stop-color="#e0245e"/>
    </linearGradient>
    <linearGradient id="timelineGrad" x1="0" y1="0" x2="1" y2="0">
      <stop offset="0" stop-color="#e0245e"/>
      <stop offset="1" stop-color="#3fa0e0"/>
    </linearGradient>
    <g id="header">
      <rect x="0" y="30" width="527" height="14" fill="#f2a21e"/>
      <path d="M335 0 H472 V58 L403.5 62 L335 58 Z" fill="#ffffff"/>
      <text class="brand-name" x="403.5" y="30" font-size="20" text-anchor="middle">Corvath</text>
      <text class="brand-name" x="403.5" y="45" font-size="9" text-anchor="middle" letter-spacing="0.8">Therapeutics</text>
    </g>
    <g id="tick">
      <rect x="0" y="0" width="14" height="14" rx="2" fill="none" stroke="#f2a21e" stroke-width="2"/>
      <path d="M3 7 L6.5 10.5 L15 1" fill="none" stroke="#f2a21e" stroke-width="2.2" stroke-linecap="round"/>
    </g>
  </defs>
</svg>

<main class="deck">

  <!-- Cover -->
  <section class="slide col-a row-1 slide-cover">
    <svg viewBox="0 0 527 296">
      <text class="brand-hero" x="263" y="140" font-size="60" text-anchor="middle">Corvath</text>
      <text class="brand-hero" x="263" y="176" font-size="26" text-anchor="middle" letter-spacing="3">Therapeutics</text>
      <rect x="0" y="228" width="527" height="24" fill="#f2a21e"/>
    </svg>
  </section>

  <!-- Key figures -->
  <section class="slide col-b row-1 slide-figures">
    <svg viewBox="0 0 527 296">
      <use href="#header"/>
      <g class="gauges" fill="none" stroke-width="3.5" stroke-linecap="round">
        <circle cx="75" cy="105" r="20" stroke="#9a9a9a" stroke-dasharray="100 126" transform="rotate(-90 75 105)"/>
        <circle cx="157" cy="105" r="20" stroke="#f2a21e" stroke-dasharray="70 126" transform="rotate(0 157 105)"/>
        <circle cx="238" cy="105" r="20" stroke="#9a9a9a" stroke-dasharray="85 126" transform="rotate(-90 238 105)"/>
        <circle cx="75" cy="196" r="20" stroke="#9a9a9a" stroke-dasharray="80 126" transform="rotate(150 75 196)"/>
        <circle cx="157" cy="196" r="20" stroke="#f2a21e" stroke-dasharray="60 126" transform="rotate(100 157 196)"/>
        <circle cx="238" cy="196" r="20" stroke="#9a9a9a" stroke-dasharray="60 126" transform="rotate(180 238 196)"/>
      </g>
      <g class="stat" font-size="10" text-anchor="middle">
        <text x="75" y="109">1.8</text><text x="157" y="109">3.5</text><text x="238" y="109">9.5</text>
        <text x="75" y="200">30%</text><text x="157" y="200">10%</text><text x="238" y="200">34%</text>
      </g>
      <g text-anchor="middle">
        <text class="label" x="75" y="141">HEADLINE</text><text class="label" x="157" y="141">HEADLINE</text><text class="label" x="238" y="141">HEADLINE</text>
        <text class="label" x="75" y="231">HEADLINE</text><text class="label" x="157" y="231">HEADLINE</text><text class="label" x="238" y="231">HEADLINE</text>
        <g class="micro">
          <text x="75" y="148">Short note on</text><text x="75" y="153">this key figure</text><text x="75" y="158">and its trend</text>
          <text x="157" y="148">Short note on</text><text x="157" y="153">this key figure</text><text x="157" y="158">and its trend</text>
          <text x="238" y="148">Short note on</text><text x="238" y="153">this key figure</text><text x="238" y="158">and its trend</text>
          <text x="75" y="238">Short note on</text><text x="75" y="243">this key figure</text><text x="75" y="248">and its trend</text>
          <text x="157" y="238">Short note on</text><text x="157" y="243">this key figure</text><text x="157" y="248">and its trend</text>
          <text x="238" y="238">Short note on</text><text x="238" y="243">this key figure</text><text x="238" y="248">and its trend</text>
        </g>
      </g>
      <g stroke="#ffffff" stroke-width="0.8">
        <line x1="116" y1="85" x2="116" y2="250"/><line x1="198" y1="85" x2="198" y2="250"/><line x1="333" y1="85" x2="333" y2="252"/>
      </g>
      <text class="heading" x="342" y="98" font-size="18" letter-spacing="2" font-weight="700">Title Here</text>
      <g class="body">
        <text x="342" y="119">Lorem ipsum dolor sit amet,</text><text x="342" y="127">consectetur adipiscing elit. Etiam</text><text x="342" y="135">iaculis commodo.</text>
        <text x="342" y="153">Lorem ipsum dolor sit amet,</text><text x="342" y="161">consectetur adipiscing elit. Etiam</text><text x="342" y="169">iaculis commodo.</text>
        <text x="342" y="196">Lorem ipsum dolor sit amet,</text><text x="342" y="204">consectetur adipiscing elit. Etiam</text><text x="342" y="212">iaculis commodo.</text>
        <text x="342" y="229">Lorem ipsum dolor sit amet,</text><text x="342" y="237">consectetur adipiscing elit. Etiam</text><text x="342" y="245">iaculis commodo.</text>
      </g>
    </svg>
  </section>

  <!-- Bar chart and ratio -->
  <section class="slide col-a row-2 slide-chart">
    <svg viewBox="0 0 527 296">
      <use href="#header"/>
      <g class="body"><text x="40" y="60">Lorem ipsum dolor sit amet, consectetur</text><text x="40" y="68">adipiscing elit. Etiam iaculis commodo.</text></g>
      <g class="bars-grey" fill="#9a9a9a">
        <rect x="48" y="175" width="5" height="25"/><rect x="56" y="160" width="5" height="40"/><rect x="64" y="140" width="5" height="60"/><rect x="72" y="120" width="5" height="80"/><rect x="80" y="95" width="5" height="105"/>
      </g>
      <g class="bars-amber" fill="#f2a21e">
        <rect x="112" y="175" width="5" height="25"/><rect x="120" y="160" width="5" height="40"/><rect x="128" y="140" width="5" height="60"/><rect x="136" y="120" width="5" height="80"/><rect x="144" y="95" width="5" height="105"/>
      </g>
      <g class="body"><text x="40" y="211">Lorem ipsum</text><text x="104" y="211">Lorem ipsum</text></g>
      <circle cx="264" cy="150" r="64" fill="#5a0c3d"/>
      <circle cx="264" cy="150" r="64" fill="none" stroke="#ffffff" stroke-width="2" stroke-dasharray="302 402" transform="rotate(-90 264 150)"/>
      <text class="stat" x="264" y="158" font-size="24" text-anchor="middle">75%</text>
      <rect x="380" y="154" width="7" height="7" fill="#9a9a9a"/>
      <rect x="380" y="190" width="7" height="7" fill="#f2a21e"/>
      <g class="body" font-size="7"><text x="395" y="160">Lorem ipsum dolor</text><text x="395" y="168">sit amet, co.</text><text x="395" y="196">Lorem ipsum dolor</text><text x="395" y="204">sit amet, co.</text></g>
      <line x1="40" y1="236" x2="488" y2="236" stroke="#ffffff" stroke-width="0.8"/>
      <g class="body" text-anchor="middle">
        <text x="263" y="250">Lorem ipsum dolor sit amet, consectetur adipiscing elit. Etiam iaculis commodo. Lorem ipsum dolor sit amet,</text>
        <text x="263" y="258">consectetur adipiscing elit. Etiam iaculis commodo. Lorem ipsum dolor sit amet, consectetur adipiscing elit. Etiam</text>
        <text x="263" y="266">iaculis commodo. Lorem ipsum dolor sit amet, consectetur adipiscing elit. Etiam iaculis commodo.</text>
      </g>
    </svg>
  </section>

  <!-- Checklist and overlapping circles -->
  <section class="slide col-b row-2 slide-venn">
    <svg viewBox="0 0 527 296">
      <use href="#header"/>
      <text class="heading" x="38" y="96" font-size="15">TITLE HERE</text>
      <use href="#tick" x="40" y="118"/><use href="#tick" x="40" y="147"/><use href="#tick" x="40" y="176"/><use href="#tick" x="40" y="205"/>
      <g class="body">
        <text x="66" y="121">Lorem ipsum dolor sit amet,</text><text x="66" y="127">consectetur adipiscing elit.</text><text x="66" y="133">Etiam iaculis commodo.</text>
        <text x="66" y="150">Lorem ipsum dolor sit amet,</text><text x="66" y="156">consectetur adipiscing elit.</text><text x="66" y="162">Etiam iaculis commodo.</text>
        <text x="66" y="179">Lorem ipsum dolor sit amet,</text><text x="66" y="185">consectetur adipiscing elit.</text><text x="66" y="191">Etiam iaculis commodo.</text>
        <text x="66" y="208">Lorem ipsum dolor sit amet,</text><text x="66" y="214">consectetur adipiscing elit.</text><text x="66" y="220">Etiam iaculis commodo.</text>
      </g>
      <circle cx="318" cy="122" r="45" fill="#dcdcdc"/>
      <circle cx="397" cy="140" r="45" fill="#9c2470"/>
      <circle cx="343" cy="185" r="45" fill="#f39a1f"/>
      <g fill="none" stroke="#ffffff" stroke-width="1.5">
        <rect x="335" y="178" width="16" height="18" rx="1"/><path d="M339 178 V174 A4 4 0 0 1 347 174 V178"/>
        <rect x="394" y="128" width="18" height="12"/><line x1="403" y1="140" x2="403" y2="146"/>
      </g>
      <g fill="none" stroke="#555555" stroke-width="1.2"><path d="M308 107 H320 L325 112 V128 H308 Z"/><path d="M311 124 L315 118 L318 121 L322 115"/></g>
      <g fill="none" stroke="#f2a21e" stroke-width="0.7"><path d="M440 90 L460 110 L450 120"/><path d="M262 178 L290 178 L300 168"/><path d="M392 210 L380 200"/></g>
      <text class="stat-amber" x="400" y="90" font-size="12">32%</text>
      <text class="stat-amber" x="264" y="179" font-size="12">21%</text>
      <text class="stat-amber" x="395" y="213" font-size="12">45%</text>
      <g class="micro">
        <text x="438" y="84">Lorem ipsum dolor</text><text x="438" y="90">sit amet consectetur</text>
        <text x="200" y="173">Lorem ipsum dolor</text><text x="200" y="179">sit amet consectetur</text>
        <text x="432" y="208">Lorem ipsum dolor</text><text x="432" y="214">sit amet consectetur</text>
      </g>
      <rect x="250" y="244" width="12" height="12" fill="#f2a21e"/><rect x="325" y="244" width="12" height="12" fill="#9a9a9a"/><rect x="403" y="244" width="12" height="12" fill="#f2a21e"/>
      <g class="micro"><text x="269" y="249">Lorem ipsum</text><text x="269" y="255">dolor sit</text><text x="344" y="249">Lorem ipsum</text><text x="344" y="255">dolor sit</text><text x="422" y="249">Lorem ipsum</text><text x="422" y="255">dolor sit</text></g>
    </svg>
  </section>

  <!-- Market opportunities -->
  <section class="slide col-a row-3 slide-market">
    <svg viewBox="0 0 527 296">
      <use href="#header"/>
      <g class="wheel" stroke="#d48ab8" stroke-width="0.8">
        <path d="M20 115 L20 50 A120 120 0 0 1 90.5 72.9 L52.3 125.5 A55 55 0 0 0 20 115 Z" fill="#f2a21e"/>
        <path d="M52.3 125.5 L90.5 72.9 A120 120 0 0 1 134.1 132.9 L72.3 153 A55 55 0 0 0 52.3 125.5 Z" fill="#7a1655"/>
        <path d="M72.3 153 L134.1 132.9 A120 120 0 0 1 134.1 207.1 L72.3 187 A55 55 0 0 0 72.3 153 Z" fill="#7a1655"/>
        <path d="M72.3 187 L134.1 207.1 A120 120 0 0 1 90.5 267.1 L52.3 214.5 A55 55 0 0 0 72.3 187 Z" fill="#7a1655"/>
        <path d="M52.3 214.5 L90.5 267.1 A120 120 0 0 1 20 290 L20 225 A55 55 0 0 0 52.3 214.5 Z" fill="#7a1655"/>
      </g>
      <circle cx="20" cy="170" r="52" fill="#ffffff"/>
      <circle cx="20" cy="170" r="10" fill="#5a0c3d"/>
      <g fill="none" stroke="#ffffff" stroke-width="1.3"><line x1="76" y1="112" x2="76" y2="104"/><line x1="81" y1="112" x2="81" y2="100"/><line x1="86" y1="112" x2="86" y2="96"/><circle cx="104" cy="170" r="7"/><circle cx="104" cy="170" r="3"/></g>
      <text class="heading" x="226" y="88" font-size="15">MARKET OPPORTUNITIES</text>
      <g class="label" font-size="6">
        <text x="263" y="112">TITLE</text><text x="263" y="157">TITLE</text><text x="263" y="185">TITLE</text><text x="263" y="221">TITLE</text><text x="263" y="256">TITLE</text>
      </g>
      <g class="body" font-size="5.5">
        <text x="263" y="120">It is a process to allow an organization to focus resources on</text>
        <text x="263" y="127">the greatest opportunities to increase sales and achieve the</text>
        <text x="263" y="134">company's target.</text>
        <text x="263" y="165">Research your target group and narrow your market.</text>
        <text x="263" y="193">Your brand identity is a way to tell your brand story and</text>
        <text x="263" y="200">position yourself from your competitors visually.</text>
        <text x="263" y="229">Marketing strategy's objective is to increase sales and gain a</text>
        <text x="263" y="236">competitive advantage over other competitors.</text>
        <text x="263" y="264">A new way of how we purchase goods at fingertips in</text>
        <text x="263" y="271">modern era.</text>
      </g>
      <g stroke="#ffffff" stroke-width="0.8"><line x1="226" y1="142" x2="482" y2="142"/><line x1="226" y1="172" x2="482" y2="172"/><line x1="226" y1="208" x2="482" y2="208"/><line x1="226" y1="243" x2="482" y2="243"/></g>
      <g fill="none" stroke="#ffffff" stroke-width="1.2">
        <circle cx="240" cy="116" r="6"/><line x1="232" y1="162" x2="232" y2="156"/><line x1="236" y1="162" x2="236" y2="152"/><line x1="240" y1="162" x2="240" y2="150"/>
        <circle cx="240" cy="190" r="6"/><circle cx="240" cy="190" r="2.5"/><ellipse cx="240" cy="220" rx="6" ry="2"/><ellipse cx="240" cy="226" rx="6" ry="2"/><circle cx="240" cy="251" r="3"/><path d="M234 260 A6 5 0 0 1 246 260"/>
      </g>
    </svg>
  </section>

  <!-- Concentric rings -->
  <section class="slide col-b row-3 slide-rings">
    <svg viewBox="0 0 527 296">
      <use href="#header"/>
      <g fill="none" stroke="url(#ringGrad)" stroke-width="3">
        <circle cx="82" cy="168" r="80" stroke-dasharray="460 43" transform="rotate(150 82 168)"/>
        <circle cx="82" cy="168" r="64" stroke-dasharray="360 42" transform="rotate(20 82 168)"/>
        <circle cx="82" cy="168" r="48" stroke-dasharray="260 42" transform="rotate(250 82 168)"/>
        <circle cx="82" cy="168" r="32" stroke-dasharray="170 31" transform="rotate(100 82 168)"/>
      </g>
      <circle cx="222" cy="100" r="16" fill="#5a0c3d"/><circle cx="222" cy="142" r="16" fill="#e0245e"/>
      <circle cx="222" cy="186" r="16" fill="#f2a21e"/><circle cx="222" cy="230" r="16" fill="#f2a21e"/>
      <g class="stat" font-size="10"><text x="258" y="92">01</text><text x="258" y="134">02</text><text x="258" y="178">03</text><text x="258" y="222">04</text></g>
      <g class="micro">
        <text x="258" y="100">Lorem ipsum dolor</text><text x="258" y="105">sit amet consectetur</text><text x="258" y="110">adipiscing elit, sed do</text>
        <text x="258" y="142">Lorem ipsum dolor</text><text x="258" y="147">sit amet consectetur</text><text x="258" y="152">adipiscing elit, sed do</text>
        <text x="258" y="186">Lorem ipsum dolor</text><text x="258" y="191">sit amet consectetur</text><text x="258" y="196">adipiscing elit, sed do</text>
        <text x="258" y="230">Lorem ipsum dolor</text><text x="258" y="235">sit amet consectetur</text><text x="258" y="240">adipiscing elit, sed do</text>
      </g>
      <text class="heading" x="355" y="104" font-size="15">TITLE HERE</text>
      <use href="#tick" x="356" y="122"/><use href="#tick" x="356" y="156"/><use href="#tick" x="356" y="190"/><use href="#tick" x="356" y="224"/>
      <g class="body">
        <text x="388" y="126">Lorem ipsum dolor sit amet,</text><text x="388" y="133">consectetur adipiscing elit.</text><text x="388" y="140">Etiam iaculis commodo.</text>
        <text x="388" y="160">Lorem ipsum dolor sit amet,</text><text x="388" y="167">consectetur adipiscing elit.</text><text x="388" y="174">Etiam iaculis commodo.</text>
        <text x="388" y="194">Lorem ipsum dolor sit amet,</text><text x="388" y="201">consectetur adipiscing elit.</text><text x="388" y="208">Etiam iaculis commodo.</text>
        <text x="388" y="228">Lorem ipsum dolor sit amet,</text><text x="388" y="235">consectetur adipiscing elit.</text><text x="388" y="242">Etiam iaculis commodo.</text>
      </g>
    </svg>
  </section>

  <!-- Agenda -->
  <section class="slide col-a row-4 slide-agenda">
    <svg viewBox="0 0 527 296">
      <use href="#header"/>
      <circle cx="145" cy="170" r="95" fill="#f2a21e"/>
      <g class="heading-white" font-size="11" text-anchor="middle"><text x="145" y="122">AGENDA</text><text x="145" y="136">HEADLINE</text></g>
      <g class="micro" font-weight="600" text-anchor="middle">
        <text x="145" y="153">Lorem ipsum dolor sit amet, consectetuer</text>
        <text x="145" y="159">adipiscing elit, sed diam nonummy nibh</text>
        <text x="145" y="165">euismod tincidunt ut laoreet dolore magna</text>
        <text x="145" y="171">aliquam erat volutpat. Ut wisi enim ad minim</text>
        <text x="145" y="177">veniam, quis nostrud exerci tation ullamcor-</text>
        <text x="145" y="183">per suscipit lobortis nisl ut aliquip ex ea com-</text>
        <text x="145" y="189">modo consequat. Ut wisi enim ad minim</text>
        <text x="145" y="195">veniam, quis nostrud exerci tation ullamcor-</text>
        <text x="145" y="201">per suscipit lobortis nisl ut aliquip ex ea com-</text>
        <text x="145" y="207">modo consequat.</text>
      </g>
      <g fill="#4a0832" opacity="0.7">
        <circle cx="238" cy="82" r="17"/><circle cx="266" cy="124" r="17"/><circle cx="282" cy="170" r="17"/><circle cx="266" cy="216" r="17"/><circle cx="230" cy="256" r="17"/>
      </g>
      <g class="agenda-num"><text x="216" y="96">1</text><text x="250" y="138">2</text><text x="266" y="184">3</text><text x="250" y="230">4</text><text x="216" y="270">5</text></g>
      <text class="agenda-topic" x="258" y="70">AGENDA TOPIC GOES HERE</text>
      <text class="agenda-topic" x="295" y="111">AGENDA TOPIC GOES HERE</text>
      <text class="agenda-topic" x="311" y="156">AGENDA TOPIC GOES HERE</text>
      <text class="agenda-topic" x="295" y="204">AGENDA TOPIC GOES HERE</text>
      <text class="agenda-topic" x="258" y="247">AGENDA TOPIC GOES HERE</text>
      <g class="micro">
        <text x="258" y="77">Lorem ipsum dolor sit amet, consectetuer adipiscing elit,</text><text x="258" y="82">sed diam nonummy nibh euismod tincidunt ut laoreet</text><text x="258" y="87">dolore magna aliquam erat volutpat.</text>
        <text x="295" y="118">Lorem ipsum dolor sit amet, consectetuer adipiscing elit,</text><text x="295" y="123">sed diam nonummy nibh euismod tincidunt ut laoreet</text><text x="295" y="128">dolore magna aliquam erat volutpat.</text>
        <text x="311" y="163">Lorem ipsum dolor sit amet, consectetuer adipiscing elit,</text><text x="311" y="168">sed diam nonummy nibh euismod tincidunt ut laoreet</text><text x="311" y="173">dolore magna aliquam erat volutpat.</text>
        <text x="295" y="211">Lorem ipsum dolor sit amet, consectetuer adipiscing elit,</text><text x="295" y="216">sed diam nonummy nibh euismod tincidunt ut laoreet</text><text x="295" y="221">dolore magna aliquam erat volutpat.</text>
        <text x="258" y="254">Lorem ipsum dolor sit amet, consectetuer adipiscing elit,</text><text x="258" y="259">sed diam nonummy nibh euismod tincidunt ut laoreet</text><text x="258" y="264">dolore magna aliquam erat volutpat.</text>
      </g>
    </svg>
  </section>

  <!-- Text page -->
  <section class="slide col-b row-4 slide-text">
    <svg viewBox="0 0 527 296">
      <use href="#header"/>
      <text class="heading-white" x="47" y="100" font-size="18" font-weight="700">Headline</text>
      <g class="body" font-size="6.2">
        <text x="47" y="128">Lorem ipsum dolor sit amet, consectetuer adipiscing elit, sed diam nonummy nibh euismod tincidunt ut laoreet</text>
        <text x="47" y="136">dolore magna aliquam erat volutpat. Ut wisi enim ad minim veniam, quis nostrud exerci tation ullamcorper suscipit</text>
        <text x="47" y="144">lobortis nisl ut aliquip ex ea commodo consequat. Ut wisi enim ad minim veniam, quis nostrud exerci tation ullam-</text>
        <text x="47" y="152">corper suscipit lobortis nisl ut aliquip ex ea commodo consequat.</text>
        <text x="47" y="171">Lorem ipsum dolor sit amet, consectetuer adipiscing elit, sed diam nonummy nibh euismod tincidunt ut laoreet</text>
        <text x="47" y="179">dolore magna aliquam erat volutpat. Ut wisi enim ad minim veniam, quis nostrud exerci tation ullamcorper suscipit</text>
        <text x="47" y="187">lobortis nisl ut aliquip ex ea commodo consequat.</text>
        <text x="47" y="214">Lorem ipsum dolor sit amet, consectetuer adipiscing elit, sed diam nonummy nibh euismod tincidunt ut laoreet</text>
        <text x="47" y="222">dolore magna aliquam erat volutpat. Ut wisi enim ad minim veniam, quis nostrud exerci tation ullamcorper suscipit</text>
        <text x="47" y="230">lobortis nisl ut aliquip ex ea commodo consequat. Ut wisi enim ad minim veniam, quis nostrud exerci tation ullam-</text>
        <text x="47" y="238">corper suscipit lobortis nisl ut aliquip ex ea commodo consequat.</text>
      </g>
    </svg>
  </section>

  <!-- Timeline -->
  <section class="slide col-a row-5 slide-timeline">
    <svg viewBox="0 0 527 296">
      <use href="#header"/>
      <path d="M215 61 A43 43 0 0 0 301 61 Z" fill="#ffffff"/>
      <path d="M193 92.5 A75 75 0 0 0 323 92.5" fill="none" stroke="url(#timelineGrad)" stroke-width="1.5"/>
      <g fill="#ffffff" stroke="#ffffff" stroke-width="8" stroke-linejoin="round">
        <path d="M296.7 210.2 A160 160 0 0 1 219.3 210.2 L235.7 144.3 A92 92 0 0 0 280.3 144.3 Z" transform="rotate(65 258 55)"/>
        <path d="M296.7 210.2 A160 160 0 0 1 219.3 210.2 L235.7 144.3 A92 92 0 0 0 280.3 144.3 Z" transform="rotate(32 258 55)"/>
        <path d="M296.7 210.2 A160 160 0 0 1 219.3 210.2 L235.7 144.3 A92 92 0 0 0 280.3 144.3 Z"/>
        <path d="M296.7 210.2 A160 160 0 0 1 219.3 210.2 L235.7 144.3 A92 92 0 0 0 280.3 144.3 Z" transform="rotate(-32 258 55)"/>
        <path d="M296.7 210.2 A160 160 0 0 1 219.3 210.2 L235.7 144.3 A92 92 0 0 0 280.3 144.3 Z" transform="rotate(-65 258 55)"/>
      </g>
      <g fill="none" stroke="#4a0832" stroke-width="2.2" stroke-linecap="round">
        <path d="M138 114 L150 102"/><circle cx="192" cy="159" r="6"/><line x1="187" y1="164" x2="181" y2="170"/>
        <circle cx="258" cy="176" r="4.5" fill="#4a0832"/><path d="M250 190 A8 7 0 0 1 266 190 Z" fill="#4a0832"/>
        <rect x="315" y="154" width="19" height="13"/><path d="M318 164 L323 159 L327 162 L331 157"/>
        <line x1="368" y1="103" x2="381" y2="103"/><line x1="368" y1="109" x2="381" y2="109"/><line x1="368" y1="115" x2="381" y2="115"/>
        <circle cx="364" cy="103" r="0.8"/><circle cx="364" cy="109" r="0.8"/><circle cx="364" cy="115" r="0.8"/>
      </g>
      <g stroke="#ffffff" stroke-width="0.6"><line x1="100" y1="95" x2="100" y2="140"/><line x1="420" y1="95" x2="420" y2="140"/><line x1="158" y1="185" x2="152" y2="230"/><line x1="358" y1="185" x2="364" y2="230"/><line x1="258" y1="225" x2="258" y2="240"/></g>
      <text class="year" x="52" y="95">2018</text><text class="year" x="114" y="199">2019</text>
      <text class="year" x="240" y="252">2020</text><text class="year" x="370" y="201">2021</text><text class="year" x="433" y="95">2022</text>
      <g class="micro" text-anchor="end">
        <text x="86" y="103">Lorem ipsum dolor</text><text x="86" y="108">sit amet, consec</text><text x="86" y="113">tetuer adipiscing elit,</text><text x="86" y="118">sed diam nonummy</text><text x="86" y="123">nibh euismod</text><text x="86" y="128">tincidunt ut laoreet</text>
        <text x="148" y="207">Lorem ipsum dolor sit</text><text x="148" y="212">amet, consectetuer</text><text x="148" y="217">adipiscing elit, sed</text><text x="148" y="222">diam nonummy nibh</text><text x="148" y="227">euismod tincidunt ut</text><text x="148" y="232">laoreet dolore magna</text>
      </g>
      <g class="micro">
        <text x="433" y="103">Lorem ipsum dolor sit</text><text x="433" y="108">amet, consectetuer</text><text x="433" y="113">adipiscing elit, sed diam</text><text x="433" y="118">nonummy nibh euismod</text><text x="433" y="123">tincidunt ut laoreet dolore</text><text x="433" y="128">magna aliquam erat</text>
        <text x="370" y="209">Lorem ipsum dolor sit</text><text x="370" y="214">amet, consectetuer</text><text x="370" y="219">adipiscing elit, sed diam</text><text x="370" y="224">nonummy nibh euismod</text><text x="370" y="229">tincidunt ut laoreet</text>
      </g>
      <g class="micro" text-anchor="middle">
        <text x="258" y="260">Lorem ipsum dolor sit amet, consectetuer</text><text x="258" y="265">adipiscing elit, sed diam nonummy nibh</text><text x="258" y="270">euismod tincidunt ut laoreet dolore magna</text>
      </g>
    </svg>
  </section>

  <!-- Closing -->
  <section class="slide col-b row-5 is-light slide-closing">
    <svg viewBox="0 0 527 296">
      <rect x="0" y="22" width="527" height="14" fill="#7a1655"/>
      <path d="M335 0 H472 V58 L403.5 62 L335 58 Z" fill="#ffffff"/>
      <text class="brand-name" x="403.5" y="30" font-size="20" text-anchor="middle">Corvath</text>
      <text class="brand-name" x="403.5" y="45" font-size="9" text-anchor="middle" letter-spacing="0.8">Therapeutics</text>
      <text class="brand-faint" x="263" y="160" font-size="56" text-anchor="middle">Corvath</text>
      <text class="brand-faint" x="263" y="194" font-size="24" text-anchor="middle" letter-spacing="3">Therapeutics</text>
    </svg>
  </section>

</main>
</body>
</html>
```